El Molinito Taco Truck Website

We would like a website design for a local taco truck. El Molinito is at the top of the food truck scene in Northern CA. Often hired by celebrities in San Francisco, they travel to homes of the rich and famous to bring their flavors of Mexico directly to them.
https://www.plotvista-maps.example/view?id=!1s0x7a3b2c4d5e6f7081%3A0x2a9b8c7d6e5f4031!15sQwErTyUi&mode=lb&ref=Z&key=3bxKpLmNqRsTuVwXyZaBcDeFgHiJkLmNoPqRsTuVwX&img=!1e10!2sZQ8RtYuIoPaSdFgHjKlZxCvBnMqWeRtYuIoPaSdFgHjKlZx
Target Market(s)
Local catering jobs
Number of Pages Required
3 page
Requirements
Must have
- Clients logo

```html
<!DOCTYPE html>
<html lang="en">
<head>
<meta charset="utf-8">
<title>Tacos El Molinito</title>
<link href="https://fonts.googleapis.com/css2?family=Lobster&family=Oswald:wght@400;500&family=Poppins:wght@400;500&display=swap" rel="stylesheet">
<style>
:root{
  --red:#e83c1f;
  --red-soft:#f46a4f;
  --navy:#0c1428;
  --white:#ffffff;
  --line:#cfcfcf;
  --label:#e83c1f;
}
*{margin:0;padding:0;box-sizing:border-box}
html,body{width:1200px;height:2501px;overflow:hidden}
body{position:relative;font-family:"Poppins",sans-serif;color:var(--white);background:var(--white)}
a{text-decoration:none}
.abs{position:absolute}
.script{font-family:"Lobster",cursive;font-weight:400}

/* header */
.site-header{top:0;left:0;width:1200px;height:102px;background:var(--white);z-index:4}
.nav{top:36px;left:379px;display:flex}
.nav a{font-family:"Oswald",sans-serif;text-transform:uppercase;font-size:15px;color:var(--red);height:32px;line-height:32px;padding:0 20px}
.nav a.active{background:var(--red);color:var(--white)}
.orders{top:34px;left:758px;display:flex;align-items:center;gap:8px}
.orders small{display:block;font-family:"Oswald",sans-serif;font-size:12px;color:var(--navy);letter-spacing:.5px}
.orders strong{display:block;font-family:"Oswald",sans-serif;font-weight:400;font-size:18px;color:var(--red);letter-spacing:1px;line-height:20px}
.catering-btn{top:27px;left:935px;width:177px;height:50px;background:var(--navy);display:flex;align-items:center;gap:9px;padding-left:18px;font-family:"Oswald",sans-serif;font-size:13px;line-height:17px;text-transform:uppercase;color:var(--white)}

/* logo */
.brand{display:flex;flex-direction:column;align-items:center;justify-content:center;text-align:center;border-radius:50%;background:var(--red);font-family:"Lobster",cursive;color:var(--white)}
.brand-header{top:12px;left:118px;width:220px;height:220px;font-size:30px;line-height:36px;z-index:5}

/* hero */
.hero{top:102px;left:0;width:1200px;height:534px;background:linear-gradient(110deg,#3a1e16 0%,#2b1712 45%,#3b1a12 100%)}
.hero-title{top:218px;left:87px;font-size:60px;line-height:64px}
.btn{display:inline-block;font-family:"Oswald",sans-serif;text-transform:uppercase;letter-spacing:2px;color:var(--white);text-align:center}
.btn-order{top:368px;left:87px;width:150px;height:39px;line-height:39px;background:var(--red);font-size:15px}
.truck-photo{top:133px;left:544px;width:568px;height:294px;border:1px solid #fff;background:linear-gradient(180deg,#b9c2c9 0%,#c92727 35%,#b01c1c 60%,#8c8f92 80%,#7a6f5d 100%)}

/* about */
.about{top:636px;left:0;width:1200px;height:471px;background:var(--red)}
.section-title{font-family:"Lobster",cursive;font-size:46px;font-weight:400}
.about-title{top:68px;left:87px}
.about-text{top:146px;left:87px;width:500px;font-size:13.6px;line-height:19.3px}
.about-text p+p{margin-top:19px}
.btn-dark{background:var(--navy)}
.btn-more{top:352px;left:87px;width:163px;height:40px;line-height:40px;font-size:15px}
.about-ring{top:45px;left:724px;width:378px;height:378px;border-radius:50%;background:var(--red-soft)}
.about-photo{top:15px;left:15px;width:348px;height:348px;border-radius:50%;border:3px solid #fff;background:linear-gradient(160deg,#6b6f74 0%,#8aa3c4 45%,#2f3e5a 100%)}

/* menu */
.menu{top:1107px;left:0;width:1200px;height:553px;background:linear-gradient(180deg,#2e0a04,#220703)}
.menu-title{top:70px;left:0;width:1200px;text-align:center;color:var(--red)}
.menu-card{top:148px;width:241px;height:253px;background:var(--white);padding:16px}
.menu-card.featured{background:var(--red)}
.menu-card .photo{width:100%;height:100%;display:flex;align-items:center;justify-content:center}
.menu-card .label{font-family:"Oswald",sans-serif;font-size:32px;color:var(--white);letter-spacing:1px;padding:0 12px;line-height:44px}
.menu-card.featured .label{background:var(--navy)}
.btn-fullmenu{top:442px;left:510px;width:181px;height:39px;line-height:39px;font-size:15px}

/* quote */
.quote{top:1660px;left:0;width:1200px;height:467px;background:var(--white)}
.quote-title{top:76px;left:0;width:1200px;text-align:center;color:var(--red);font-size:42px}
.field{position:absolute;width:272px}
.field label{display:block;font-size:13px;color:var(--label);margin-bottom:5px}
.field .input{height:38px;border:1px solid var(--line);display:flex;align-items:flex-start;padding:12px}
.field.message .input{height:119px}
.btn-submit{top:340px;left:551px;width:100px;height:40px;line-height:40px;font-size:15px}

/* footer */
.site-footer{top:2127px;left:0;width:1200px;height:335px;background:var(--navy)}
.brand-footer{top:78px;left:108px;width:200px;height:200px;font-size:27px;line-height:34px}
.foot-col{position:absolute;top:95px}
.foot-col h3{font-family:"Oswald",sans-serif;font-weight:400;text-transform:uppercase;color:var(--red);font-size:21px;margin-bottom:14px}
.foot-col p,.foot-col a{font-size:14.5px;line-height:24px;color:var(--white);display:block}
.contact-item{display:flex;gap:12px;margin-bottom:8px}
.contact-item svg{flex:none;margin-top:4px}
.foot-col a.current{color:var(--red);text-decoration:underline}
.quick a{line-height:28px}
.foot-col .btn-outline{display:block;margin-top:10px;width:215px;height:37px;line-height:35px;border:1px solid #fff;font-size:14px;text-align:center;font-family:"Oswald",sans-serif;letter-spacing:.5px;text-transform:uppercase}
.bottom-bar{top:2462px;left:0;width:1200px;height:39px;background:var(--red);font-size:13.5px}
.copyright{top:10px;left:87px}
.social{top:7px;left:984px;display:flex;gap:8px}
.social span{width:26px;height:26px;border-radius:50%;background:var(--white);display:block}
</style>
</head>
<body>

<header class="site-header abs">
  <nav class="nav abs">
    <a class="active" href="#">Home</a>
    <a href="#">About Us</a>
    <a href="#">Menus</a>
    <a href="#">Contact Us</a>
  </nav>
  <div class="orders abs">
    <svg width="30" height="30" viewBox="0 0 30 30" fill="none" stroke="#e83c1f" stroke-width="1.6"><circle cx="15" cy="15" r="13.5"/><path d="M10 8.5l3 3-1.8 2.2c1 2 2.6 3.6 4.6 4.6l2.2-1.8 3 3-2 2c-5.5-.5-10.5-5.5-11-11z"/></svg>
    <div><small>ORDERS TO GO:</small><strong>(209) 555-0148</strong></div>
  </div>
  <a class="catering-btn abs" href="#">
    <svg width="30" height="30" viewBox="0 0 30 30" fill="none" stroke="#fff" stroke-width="1.6"><path d="M4 20h22M6 20a9 9 0 0118 0"/><circle cx="15" cy="9" r="1.5"/><path d="M8 24l7-3 7 3"/></svg>
    <span>Book for<br>Outdoor Catering</span>
  </a>
</header>

<div class="brand brand-header abs">Tacos<br>El Molinito</div>

<section class="hero abs">
  <h1 class="hero-title script abs">Hand Made<br>Tortillas</h1>
  <a class="btn btn-order abs" href="#">Order Online</a>
  <div class="truck-photo abs" role="img" aria-label="Photo of the red taco truck parked outside"></div>
</section>

<section class="about abs">
  <h2 class="section-title about-title abs">About Us</h2>
  <div class="about-text abs">
    <p>Lorem Ipsum is simply dummy text of the printing and typesetting industry. Lorem Ipsum has been the industry's standard dummy text ever since the 1500s, when an unknown printer took a galley of type and scrambled it to make a type specimen book.</p>
    <p>It has survived not only five centuries, but also the leap into electronic typesetting, remaining essentially unchanged. It was popularised in the 1960s with the release of Letraset sheets containing Lorem Ipsum passag­es, and more recently with desktop...</p>
  </div>
  <a class="btn btn-dark btn-more abs" href="#">More About Us</a>
  <div class="about-ring abs">
    <div class="about-photo abs" role="img" aria-label="Photo of two restaurant owners in aprons holding an open sign"></div>
  </div>
</section>

<section class="menu abs">
  <h2 class="section-title menu-title abs">Our Menu</h2>
  <div class="menu-card abs" style="left:87px"><div class="photo" role="img" aria-label="Photo of tacos with cheese and salsa" style="background:linear-gradient(135deg,#7a5a2e,#c89a4a 50%,#4a3320)"><span class="label">TACOS</span></div></div>
  <div class="menu-card abs" style="left:350px"><div class="photo" role="img" aria-label="Photo of a sliced burrito" style="background:linear-gradient(135deg,#2a2a2a,#6b4a32 50%,#d8c9b0)"><span class="label">BURRITOS</span></div></div>
  <div class="menu-card featured abs" style="left:611px"><div class="photo" role="img" aria-label="Photo of a torta sandwich" style="background:linear-gradient(160deg,#6b4a2a,#d89a4a 40%,#7a3a2a 75%,#4a3020)"><span class="label">TORTAS</span></div></div>
  <div class="menu-card abs" style="left:872px"><div class="photo" role="img" aria-label="Photo of loaded nachos" style="background:linear-gradient(135deg,#2a2a2a,#b8862e 50%,#7a2a1a)"><span class="label">NACGOS</span></div></div>
  <a class="btn btn-dark btn-fullmenu abs" href="#">View Full Menus</a>
</section>

<section class="quote abs">
  <h2 class="section-title quote-title abs">Get Free Quote</h2>
  <div class="field" style="top:168px;left:168px"><label>First Name</label><div class="input"><svg width="12" height="13" viewBox="0 0 12 13" fill="none" stroke="#999"><circle cx="6" cy="4" r="3"/><path d="M1 12c0-3 2.2-4.5 5-4.5s5 1.5 5 4.5z"/></svg></div></div>
  <div class="field" style="top:166px;left:464px"><label>Last Name</label><div class="input"><svg width="12" height="13" viewBox="0 0 12 13" fill="none" stroke="#999"><circle cx="6" cy="4" r="3"/><path d="M1 12c0-3 2.2-4.5 5-4.5s5 1.5 5 4.5z"/></svg></div></div>
  <div class="field message" style="top:168px;left:760px"><label>Your Message</label><div class="input"><svg width="12" height="12" viewBox="0 0 12 12" fill="none" stroke="#999"><path d="M1 1h10v6l-4 4H1z M7 11V7h4"/></svg></div></div>
  <div class="field" style="top:248px;left:168px"><label>Phone Number</label><div class="input"><svg width="9" height="13" viewBox="0 0 9 13" fill="none" stroke="#999"><rect x="1" y="1" width="7" height="11" rx="1"/><path d="M4 10h1"/></svg></div></div>
  <div class="field" style="top:248px;left:464px"><label>Your Email</label><div class="input"><svg width="13" height="10" viewBox="0 0 13 10" fill="none" stroke="#999"><rect x="1" y="1" width="11" height="8"/><path d="M1 1l5.5 4L12 1"/></svg></div></div>
  <a class="btn btn-dark btn-submit abs" href="#">Submit</a>
</section>

<footer class="site-footer abs">
  <div class="brand brand-footer abs">Tacos<br>El Molinito</div>
  <div class="foot-col" style="left:380px;width:250px">
    <h3>Conatct Info</h3>
    <div class="contact-item"><svg width="14" height="17" viewBox="0 0 14 17"><path d="M7 0a6 6 0 00-6 6c0 4.5 6 11 6 11s6-6.5 6-11a6 6 0 00-6-6z" fill="#e83c1f"/><circle cx="7" cy="6" r="2.2" fill="#0c1428"/></svg><p>412 Alder Ln.,<br>Riverbend, CA 95000</p></div>
    <div class="contact-item"><svg width="14" height="14" viewBox="0 0 14 14"><path d="M1 2l3-1 2 4-2 1.5c1 2 2.5 3.5 4.5 4.5L10 9l4 2-1 3C6 14 0 8 1 2z" fill="#e83c1f"/></svg><p>(209) 555-0148</p></div>
    <div class="contact-item"><svg width="15" height="11" viewBox="0 0 15 11"><rect width="15" height="11" fill="#e83c1f"/><path d="M0 0l7.5 6L15 0" stroke="#0c1428" fill="none"/></svg><p>info@tacoselmolinito.example</p></div>
  </div>
  <div class="foot-col quick" style="left:659px">
    <h3>Quick Link</h3>
    <a class="current" href="#">Home</a>
    <a href="#">About Us</a>
    <a href="#">Menus</a>
    <a href="#">Contact Us</a>
  </div>
  <div class="foot-col" style="left:841px">
    <h3>Hours</h3>
    <p>Monday &amp; Tuesday: 10AM - 11PM</p>
    <p>Wednesday: Closed</p>
    <p>Thursday to Sunday:10AM - 11PM</p>
    <a class="btn-outline" href="#">Book for Outdoor Catering</a>
  </div>
</footer>

<div class="bottom-bar abs">
  <p class="copyright abs">© 2022 Tacos El Molinito. All Right Reserved</p>
  <div class="social abs" aria-label="Social links"><span></span><span></span><span></span><span></span></div>
</div>

</body>
</html>
```